Re-design of Business Card

We require a design for our business card.

Korrim is a supplier of industrial packaging specializing in plastic products. We are undergoing a rebranding to appear more corporate. We have changed our company name to korrim and have a new logo.

I have uploaded our old card design with the previous company name.
Don't copy the current design. We are looking for a new design.

Industry/Entity Type

Manufacturing

Contact Information for Business Card

please don't copy the current design. we are looking for a new design.

Font styles to use
Sans Serif

Colors

Designer to choose colors to be used in the design.

Requirements
Must have
• clean and easy to read.

```html
<!DOCTYPE html>
<html lang="en">
<head>
<meta charset="utf-8">
<title>Korrim Business Card</title>
<link href="https://fonts.googleapis.com/css2?family=Open+Sans:wght@400;600;700&display=swap" rel="stylesheet">
<style>
  :root {
    --bg: #d4d6d9;
    --card: #2c2c2c;
    --map: #3b3b3b;
    --orange: #ef7a1a;
    --white: #ffffff;
  }
  * { margin: 0; padding: 0; box-sizing: border-box; }
  html, body { width: 1200px; height: 800px; overflow: hidden; }
  body {
    background: var(--bg);
    font-family: "Open Sans", Arial, sans-serif;
    color: var(--white);
    position: relative;
  }
  .card {
    position: absolute;
    width: 600px;
    height: 343px;
    background: var(--card);
    overflow: hidden;
    box-shadow: 0 6px 18px rgba(0,0,0,.25);
  }
  .card--front { left: 540px; top: 45px; }
  .card--back { left: 60px; top: 410px; }

  .brand-name {
    font-weight: 700;
    color: var(--orange);
    letter-spacing: 1px;
    line-height: 1;
  }

  /* front */
  .region-map {
    position: absolute;
    left: 100px; top: 40px;
    width: 330px; height: 270px;
    background: var(--map);
    border-radius: 40% 45% 35% 40%;
  }
  .front-brand {
    position: absolute;
    left: 150px; top: 80px;
    font-size: 62px;
  }
  .services {
    position: absolute;
    left: 110px; top: 175px;
    width: 260px;
    list-style: none;
    text-align: center;
    font-size: 15px;
    line-height: 1.5;
  }
  .services li::before {
    content: "";
    display: inline-block;
    width: 5px; height: 5px;
    border-radius: 50%;
    background: var(--orange);
    margin-right: 7px;
    vertical-align: middle;
  }
  .badges {
    position: absolute;
    right: 42px; top: 50px;
    display: flex;
    flex-direction: column;
    gap: 22px;
  }
  .badge {
    width: 72px; height: 72px;
    border-radius: 50%;
    border: 3px solid var(--orange);
  }

  /* back */
  .back-brand {
    position: absolute;
    left: 40px; top: 38px;
    font-size: 58px;
  }
  .address {
    position: absolute;
    left: 40px; top: 128px;
    font-style: normal;
    font-size: 15px;
    line-height: 1.3;
  }
  .contacts {
    position: absolute;
    left: 40px; top: 205px;
    list-style: none;
    font-size: 15px;
    line-height: 1.35;
  }
  .contacts li { display: flex; align-items: center; gap: 8px; }
  .contacts svg { width: 13px; height: 13px; flex: none; }
  .person {
    position: absolute;
    right: 40px; top: 210px;
    text-align: right;
  }
  .person__name {
    color: var(--orange);
    font-size: 21px;
    font-weight: 600;
    letter-spacing: .5px;
  }
  .person__role { font-size: 15px; }
  .edge-mark {
    position: absolute;
    right: 0; top: 206px;
    width: 14px; height: 48px;
    background: var(--orange);
  }
  .web-band {
    position: absolute;
    right: 0; bottom: 0;
    width: 300px; height: 42px;
    background: var(--orange);
    clip-path: polygon(30px 0, 100% 0, 100% 100%, 0 100%);
    display: flex;
    align-items: center;
    justify-content: center;
    font-size: 16px;
    letter-spacing: 1.5px;
  }
  .web-band b { font-weight: 700; }
</style>
</head>
<body>

<section class="card card--front">
  <div class="region-map" role="img" aria-label="Map of Australia and New Zealand"></div>
  <div class="brand-name front-brand">KORRIM</div>
  <ul class="services">
    <li>Pallet Containment</li>
    <li>Flexible Packaging</li>
    <li>Pallet Wrapping Machinery</li>
    <li>General Packaging</li>
  </ul>
  <div class="badges">
    <div class="badge" role="img" aria-label="Distribution badge"></div>
    <div class="badge" role="img" aria-label="Certification badge"></div>
    <div class="badge" role="img" aria-label="Quality standard badge"></div>
  </div>
</section>

<section class="card card--back">
  <div class="brand-name back-brand">KORRIM</div>
  <address class="address">
    48 Carrow St<br>
    Eastvale Heights, Qld<br>
    4127 Australia
  </address>
  <ul class="contacts">
    <li>
      <svg viewBox="0 0 16 16"><path fill="#ef7a1a" d="M3 1l3 3-2 2c1 2 3 4 5 5l2-2 3 3-2 3C6 14 2 10 1 3z"/></svg>
      1300 418 207
    </li>
    <li>
      <svg viewBox="0 0 16 16"><rect x="4" y="1" width="8" height="14" rx="1.5" fill="none" stroke="#ef7a1a" stroke-width="1.6"/></svg>
      0000 000 000
    </li>
    <li>
      <svg viewBox="0 0 16 16"><rect x="4" y="1" width="8" height="5" fill="#ef7a1a"/><rect x="1" y="6" width="14" height="7" rx="1" fill="#ef7a1a"/></svg>
      +61 7 3308 4152
    </li>
    <li>
      <svg viewBox="0 0 16 16"><rect x="1" y="3" width="14" height="10" fill="none" stroke="#ef7a1a" stroke-width="1.6"/><path d="M1 3l7 6 7-6" fill="none" stroke="#ef7a1a" stroke-width="1.6"/></svg>
      daniel@korrim.com.au
    </li>
  </ul>
  <div class="person">
    <div class="person__name">DANIEL REEVE</div>
    <div class="person__role">Machinery Sales Manager</div>
  </div>
  <div class="edge-mark"></div>
  <div class="web-band">www.<b>korrim</b>.com.au</div>
</section>

</body>
</html>
```